Environmental Plastics Infographic on Marine Debris

We need a series of infographics that can be used individually or as a combined presentation. We'd like the combined piece to include an introduction and conclusion along with 4-5 infographics. Each infographic (information unit) should also work as a standalone. We are trying to help people visualize size proportions and ratios to put the plastics marine debris problem in perspective. Our key point is concerning polystyrene foam which represents 35 tons. We are looking for something creative to help people understand what the problem represents in terms they are familiar with.

To view our typical company design/style please see our website at www.harbenfoamworks.org. Our primary RGB colors are: (187,140,9); (94,47,29); (94,138,164); and (164,167,15). Secondary RGB colors are (249,162,28) and (218,210,208). Our title/header font is DIN Next LT Pro and our copy font is Calibri 10.5 pt. We can deviate from the font specification if beneficial and welcome interesting text treatments and typography.

Need extra days to review

Target Market(s)

international brand manufacturers (brenloch, tavix), US legislators & government agencies

Font styles to use
Sans Serif

Requirements
Must have
• Sufficient white space. Easy to grasp message concept with visual components.

```html
<!DOCTYPE html>
<html lang="en">
<head>
<meta charset="utf-8">
<title>How Will Polystyrene Bans Improve Ocean Health?</title>
<link href="https://fonts.googleapis.com/css2?family=Barlow+Condensed:wght@500;600;700&family=Carlito:wght@400;700&family=Merriweather:wght@700&display=swap" rel="stylesheet">
<style>
:root{
  --olive:#a4a70f;
  --brown:#5e2f1d;
  --brown-dark:#4e2517;
  --blue:#5e8aa4;
  --blue-deep:#4d7892;
  --gold:#bb8c09;
  --orange:#f9a21c;
  --stone:#dad2d0;
  --ink:#231f20;
  --white:#ffffff;
}
*{margin:0;padding:0;box-sizing:border-box}
html,body{width:994px;height:1200px;overflow:hidden;background:var(--white)}
body{position:relative;font-family:"Carlito",Calibri,sans-serif;color:var(--ink)}
.abs{position:absolute}
.head{font-family:"Barlow Condensed",sans-serif;font-weight:600;text-transform:uppercase}
.ph{position:absolute;border-radius:2px}

/* intro */
.title-panel{left:12px;top:14px;width:480px;height:372px;background:var(--olive)}
.title-panel h1{position:absolute;left:26px;top:26px;color:var(--white);font-family:"Barlow Condensed",sans-serif;font-weight:600;font-size:48px;line-height:53px;letter-spacing:.5px}
.intro{left:518px;top:42px;width:456px;font-size:9.6px;line-height:12px}
.intro p{margin-bottom:11px}

/* composition */
.mass-panel{left:503px;top:189px;width:481px;height:197px;background:var(--brown);color:var(--white)}
.mass-panel .lead{position:absolute;left:16px;top:14px;font-size:11px}
.mass-panel .lead b{font-size:15.5px;margin-left:4px}
.stat{position:absolute;top:135px;display:flex;gap:4px;font-size:9.3px;line-height:12px}
.stat .pct{font-family:"Barlow Condensed",sans-serif;font-weight:500;font-size:27px;line-height:24px;color:var(--olive)}

/* scale */
.big-panel{left:11px;top:399px;width:480px;height:394px;background:var(--blue);color:var(--white)}
.big-panel .col{position:absolute;left:249px;top:0;width:48px;height:394px;background:var(--blue-deep)}
.big-panel .t1{position:absolute;left:41px;top:16px;font-size:34px;line-height:36px}
.big-panel .t2{position:absolute;left:41px;top:48px;font-size:92px;line-height:90px;font-weight:700}
.big-panel .gpgp{position:absolute;left:258px;top:128px;font-size:13px}
.row-label{position:absolute;width:120px;left:152px;text-align:center;font-size:9.3px;line-height:12px}
.row-label b{font-weight:700}
.row-pct{position:absolute;left:249px;width:48px;text-align:center;font-family:"Barlow Condensed",sans-serif;font-size:28px;font-weight:500}
.weights{position:absolute;display:flex;gap:6px;justify-content:center}
.wcap{position:absolute;left:300px;width:172px;text-align:center;font-size:9.3px}

/* news */
.news-brand{left:579px;top:413px;font-family:"Carlito",sans-serif;font-weight:700;font-size:15px;color:var(--ink)}
.news-head{left:580px;top:516px;width:142px;font-family:"Merriweather",serif;font-weight:700;font-size:8.6px;line-height:10.6px}
.news-meta{left:577px;top:561px;font-size:3.5px;color:#888}
.cars{left:744px;top:422px;width:166px;height:142px;background:var(--olive);color:var(--white);text-align:center}
.cars .lbl{font-size:11px}
.cars .val{font-size:15.5px;font-weight:700}

/* sizing */
.size-panel{left:502px;top:588px;width:480px;height:205px;background:var(--brown);color:var(--white)}
.size-panel h2{position:absolute;left:0;width:360px;top:14px;text-align:center;font-size:33px}
.size-table{position:absolute;left:36px;top:54px;border-collapse:collapse;font-size:10.3px;text-align:center}
.size-table th{background:var(--olive);font-weight:700;line-height:12px;height:36px;width:104px;border-right:1px solid var(--brown)}
.size-table td{background:var(--brown-dark);height:20.5px;border-right:1px solid var(--stone);border-top:2px solid var(--brown)}
.size-table th:last-child,.size-table td:last-child{border-right:none}
.size-note{position:absolute;left:370px;top:54px;font-size:10px;line-height:12.5px}

/* mismanaged */
.mis-title{left:70px;top:834px;font-size:33px;line-height:34px;color:var(--brown)}
.bar-label{position:absolute;width:118px;left:8px;text-align:right;font-size:10.3px;line-height:12.5px;color:var(--brown)}
.axis{position:absolute;left:138px;width:2px;background:var(--ink)}
.baseline{position:absolute;left:138px;width:320px;height:2px;background:var(--ink)}
.bar{position:absolute;left:140px;background:var(--olive);text-align:center;font-size:14.5px;color:var(--brown);line-height:24px}
.bar-text{position:absolute;left:145px;font-size:14.5px;color:var(--brown)}
.bar-pct{position:absolute;left:196px;width:200px;text-align:center;font-size:10.3px;line-height:13px;color:var(--brown)}

/* discoveries */
.disc-panel{left:502px;top:808px;width:480px;height:276px;background:var(--blue);color:var(--white)}
.disc-panel h2{position:absolute;top:20px;width:100%;text-align:center;font-size:33px}
.disc-cap{position:absolute;top:192px;width:150px;text-align:center;font-size:9.6px;line-height:14px}
.disc-cap big{font-size:16px;font-weight:700}

/* conclusion */
.closing{left:528px;top:1117px;width:440px;font-size:10.6px;line-height:12.8px;color:var(--brown);font-weight:700}
.source{left:528px;top:1161px;font-size:5.8px;color:#b01f24;font-weight:700}
</style>
</head>
<body>

<svg width="0" height="0" style="position:absolute">
  <symbol id="weight" viewBox="0 0 20 24">
    <path d="M7 5a3 3 0 0 1 6 0" fill="none" stroke="#5e2f1d" stroke-width="2"/>
    <path d="M4 7h12l3 16H1z" fill="#5e2f1d"/>
    <text x="10" y="15" font-size="5.4" font-family="Barlow Condensed,sans-serif" font-weight="700" fill="#fff" text-anchor="middle">50K</text>
    <text x="10" y="20.5" font-size="5.4" font-family="Barlow Condensed,sans-serif" font-weight="700" fill="#fff" text-anchor="middle">TON</text>
  </symbol>
</svg>

<!-- Introduction -->
<section class="abs title-panel">
  <h1>HOW WILL<br>POLYSTYRENE BANS<br>IMPROVE OCEAN<br>HEALTH?</h1>
</section>

<div class="abs intro">
  <p>A recent report looks at the role plastics play in marine debris that sheds light on previous assumptions about how different plastics contribute to the problem and where its coming from.</p>
  <p>In this ground breaking study, scientists conducted cutting-edge research at a much larger scale than had ever been done before. Over the course of three years, an international team including The Tidewater Survey Foundation, six universities, and an aerial sensor company, collected data and mapped debris fields for the Great Pacific Garbage Patch, one of the most problematic plastic pollution hot spots.</p>
  <p>Polystyrene ban legislation imply product restrictions will minimize plastic marine debris. Let’s take a closer look.</p>
</div>

<!-- GPGP composition -->
<section class="abs mass-panel">
  <p class="lead">The total plastics mass in the GPGP is projected at <b>78,908 tons</b></p>
  <div class="ph" style="left:33px;top:47px;width:62px;height:82px;background:linear-gradient(#8fa9b8,#3f6a80)" role="img" aria-label="Illustration of an abandoned fishing net, pole and boot"></div>
  <div class="ph" style="left:205px;top:52px;width:68px;height:80px;background:linear-gradient(#f1f1f1,#d59a2a 55%,#3f6a80)" role="img" aria-label="Illustration of plastic bottles and jugs"></div>
  <div class="ph" style="left:345px;top:90px;width:104px;height:42px;background:linear-gradient(#ffffff,#cfcfcf)" role="img" aria-label="Illustration of a foam tray and foam cup"></div>
  <div class="stat" style="left:11px"><span class="pct">52%</span><span>is mostly abandoned<br>fishing gear, not<br>consumer plastics.</span></div>
  <div class="stat" style="left:161px"><span class="pct">47%</span><span>is hard plastics, sheets<br>and film, making up<br>the majority of the<br>microplastics mass.</span></div>
  <div class="stat" style="left:313px"><span class="pct">.05%</span><span>is foamed plastics –<br>including polystyrene –<br>making it a minor<br>component of the GPGP.</span></div>
</section>

<!-- How big is big -->
<section class="abs big-panel">
  <div class="col"></div>
  <div class="head t1">HOW BIG IS</div>
  <div class="head t2">BIG?</div>
  <div class="head gpgp">GPGP</div>

  <div class="ph" style="left:372px;top:11px;width:50px;height:46px;background:linear-gradient(#d7d2cf,#5e2f1d)" role="img" aria-label="Icon of net and plastic bottles"></div>
  <div class="wcap" style="top:62px">All GPGP Plastics</div>
  <div class="weights" style="left:300px;width:172px;top:84px"><svg width="18" height="22"><use href="#weight"/></svg><svg width="18" height="22"><use href="#weight"/></svg></div>
  <div class="wcap" style="top:113px">78,908 tons</div>

  <div class="ph" style="left:16px;top:160px;width:114px;height:26px;background:linear-gradient(#ffffff,#e8e39a)" role="img" aria-label="Illustration of a cruise ship"></div>
  <div class="row-label" style="top:166px">1 Cruise Ship<br><b>100,000 tons</b></div>
  <div class="row-pct" style="top:162px">79%</div>
  <div class="weights" style="left:300px;width:172px;top:150px"><svg width="18" height="22"><use href="#weight"/></svg><svg width="18" height="22"><use href="#weight"/></svg></div>
  <div class="wcap" style="top:180px">100,000 tons</div>

  <div class="ph" style="left:16px;top:240px;width:114px;height:44px;background:linear-gradient(90deg,#3a4a55,#6d7d88)" role="img" aria-label="Illustration of a blue whale"></div>
  <div class="row-label" style="top:250px">1 Blue Whale<br><b>150,000 tons</b></div>
  <div class="row-pct" style="top:246px">53%</div>
  <div class="weights" style="left:300px;width:172px;top:240px"><svg width="18" height="22"><use href="#weight"/></svg><svg width="18" height="22"><use href="#weight"/></svg><svg width="18" height="22"><use href="#weight"/></svg><svg width="18" height="22"><use href="#weight"/></svg></div>
  <div class="wcap" style="top:269px">200,000 tons</div>

  <div class="ph" style="left:11px;top:298px;width:140px;height:75px;background:linear-gradient(90deg,#f9a21c,#a4a70f 35%,#5e2f1d 70%,#a4a70f)" role="img" aria-label="Illustration of the New York City skyline with a garbage truck"></div>
  <div class="row-label" style="top:330px">1 Week NYC<br>Waste Generation<br><b>269,230 tons</b></div>
  <div class="row-pct" style="top:333px">29%</div>
  <div class="weights" style="left:316px;width:160px;top:336px;justify-content:flex-start;overflow:hidden"><svg width="20" height="22"><use href="#weight"/></svg><svg width="20" height="22"><use href="#weight"/></svg><svg width="20" height="22"><use href="#weight"/></svg><svg width="20" height="22"><use href="#weight"/></svg><svg width="20" height="22"><use href="#weight"/></svg><svg width="10" height="22" viewBox="0 0 10 24" preserveAspectRatio="xMinYMin slice"><use href="#weight"/></svg></div>
  <div class="wcap" style="top:365px">269,230 tons</div>
</section>

<!-- News comparison -->
<p class="abs news-brand">Harborline Report</p>
<div class="ph" style="left:579px;top:436px;width:142px;height:76px;background:linear-gradient(#7f9db4,#1f3d5f 55%,#cdd6de)" role="img" aria-label="Photo of researchers on a ship deck sampling ocean debris"></div>
<p class="abs news-head">Great Pacific Garbage Patch weighs more than 43,000 cars and is much larger than we thought</p>
<p class="abs news-meta">Source · Mar 22 2018 · Updated Apr 16 2018 · 9:55 PM</p>
<div class="abs cars">
  <svg class="abs" style="left:-11px;top:110px" width="12" height="22"><path d="M12 0L0 22h12z" fill="#a4a70f"/></svg>
  <p class="lbl" style="margin-top:17px">Total GPGP Mass</p>
  <p class="val">&gt; 43,000 Cars</p>
  <div style="height:2px;background:var(--brown);margin:19px 0 11px"></div>
  <p class="lbl">Total Foam Plastic Mass</p>
  <p class="val">18 Cars</p>
</div>

<!-- Sizing it up -->
<section class="abs size-panel">
  <h2 class="head">Sizing It Up</h2>
  <table class="size-table">
    <tr><th>Total GPGP<br>78.9 K Tons</th><th>Marine Debris<br>Size Classes</th><th>Measurement<br>Values</th></tr>
    <tr><td>42 tons</td><td>Megaplastics</td><td>&gt;50 cm</td></tr>
    <tr><td>20 tons</td><td>Macroplastics</td><td>5 - 50 cm</td></tr>
    <tr><td>10 tons</td><td>Mesoplastics</td><td>0.5 - 5 cm</td></tr>
    <tr><td>6.5 tons</td><td>Microplastics</td><td>0.05 - 0.5 cm</td></tr>
  </table>
  <p class="size-note"><b>Mesoplastics</b><br>Think peppercorn<br>to house key.</p>
  <svg class="abs" style="left:375px;top:96px" width="80" height="76" aria-label="Peppercorn beside a house key">
    <circle cx="7" cy="22" r="4" fill="#bbb"/>
    <circle cx="41" cy="22" r="17" fill="#cfcfcf"/>
    <rect x="32" y="15" width="18" height="4" rx="2" fill="#5e2f1d"/>
    <rect x="37" y="38" width="8" height="30" fill="#cfcfcf"/>
  </svg>
</section>

<!-- Mismanaged EPS -->
<h2 class="abs head mis-title">How Much Mismanaged<br>EPS Waste Was Found?</h2>
<div class="ph" style="left:372px;top:834px;width:100px;height:82px;background:linear-gradient(#c9cfd3,#3c4b55)" role="img" aria-label="Illustration of a balance scale with a fly outweighing an elephant"></div>

<div class="axis" style="top:937px;height:80px"></div>
<p class="bar-label" style="top:941px">Worldwide Annual<br>Plastics Production</p>
<div class="bar" style="top:942px;width:313px;height:24px">320,000,000 tons</div>
<p class="bar-label" style="top:983px">Total GPGP<br>Plastics</p>
<div class="bar" style="top:984px;width:2px;height:22px"></div>
<p class="bar-text" style="top:985px">78,908 tons</p>
<div class="baseline" style="top:1016px"></div>
<p class="bar-pct" style="top:1021px">0.000024%<br>Percent of Global Production in GPGP</p>

<div class="axis" style="top:1066px;height:81px"></div>
<p class="bar-label" style="top:1062px">Worldwide Expanded<br>Polystyrene (EPS)<br>Plastics Production</p>
<div class="bar" style="top:1071px;width:313px;height:24px">6,620,000 tons</div>
<p class="bar-label" style="top:1112px">Total GPGP<br>Foam Plastics</p>
<div class="bar" style="top:1112px;width:2px;height:22px"></div>
<p class="bar-text" style="top:1113px">35 tons</p>
<div class="baseline" style="top:1145px"></div>
<p class="bar-pct" style="top:1150px">0.0000053%<br>Percent of Global Production in GPGP</p>

<!-- Surprising discoveries -->
<section class="abs disc-panel">
  <h2 class="head">Surprising Discoveries</h2>
  <div class="ph" style="left:38px;top:80px;width:100px;height:101px;background:linear-gradient(#3f7bb0,#1b3f6b)" role="img" aria-label="Illustration of a fishing net drifting underwater"></div>
  <div class="ph" style="left:188px;top:80px;width:102px;height:101px;background:linear-gradient(#4fb3d8,#e8d8a8 55%,#d8c690)" role="img" aria-label="Illustration of plastic litter on a beach"></div>
  <div class="ph" style="left:338px;top:80px;width:102px;height:101px;background:linear-gradient(135deg,#2a78b8,#9fd3ef 50%,#e9b94a)" role="img" aria-label="Illustration of a tsunami wave breaking over a coastal road"></div>
  <p class="disc-cap" style="left:13px">Approximately <big>50%</big><br>of GPGP Plastics are From<br>Marine-Based Sources.</p>
  <p class="disc-cap" style="left:164px">Beach Litter Studies<br>Were <big>Not Indicative</big><br>of GPGP Content.</p>
  <p class="disc-cap" style="left:314px"><big>20%</big> of the GPGP<br>Plastic Debris Is From the<br>2011 Tohoku Tsunami.</p>
</section>

<!-- Conclusion -->
<p class="abs closing">All Marine Plastic Debris Is A Problem! However, plastic product bans will be ineffective in reducing ocean debris. Since the U.S. contributes just 0.9% of the World’s Mismanaged Plastic Waste1,&nbsp; it is even more important to consider all parts of equation.</p>
<p class="abs source">1Source: 6 things you can do to stop plastic pollution today, Daily Ledger, September 7, 2018</p>

</body>
</html>
```